People Search Directory Needs a Web Design

We need a web design for a new web site called Kestrel Lineage Lookups. We provide free directory information, such as name, phone, address, and email. We also provide other non-white pages information such as the person's relatives, historical records to help identify the person, and link the data so people can find connections. For example, by clicking on an address that a person lives at, you can find other people who might currently (or previously) have lived at that address.

We have a very basic web page that contains a lot of public records data. The page can look very busy. We need it to be concise, where the white pages type of information is easily identifiable, but people also realize the usefulness of the surrounding data (such as possible relatives, email address, historical phone numbers, etc).

The web page also promotes an annual membership to get more in-depth information on people. These Kestrel Lineage Lookups include a criminal records check, property records, and other information.

Industry/Entity Type

Property

Requirements
Must have
• Attached is an example design we put together. We want the design to be snazzier, have more information architecture thought put into it, etc.

```html
<!DOCTYPE html>
<html lang="en">
<head>
<meta charset="utf-8">
<title>Kestrel Lineage Lookups – Marisol K Whitaker</title>
<link href="https://fonts.googleapis.com/css2?family=Source+Sans+3:wght@400;600;700&display=swap" rel="stylesheet">
<style>
:root{
  --hero-top:#2f6fb8;
  --hero-bottom:#4d95d6;
  --page-bg:#e6e7e9;
  --card-bg:#ffffff;
  --brand-blue:#1c8ccf;
  --teal:#3db7bb;
  --teal-dark:#2aa3a8;
  --lime:#9fd13a;
  --green-line:#8cc63f;
  --promo-blue:#1e8ed8;
  --text:#3c3c3c;
  --muted:#6b6b6b;
  --rule:#c9c9c9;
  --map-street:#d9d4c7;
  --map-photo:#6f7a5a;
}
*{box-sizing:border-box;margin:0;padding:0}
html,body{width:983px;height:1200px;overflow:hidden}
body{background:var(--page-bg);font-family:"Source Sans 3",Arial,sans-serif;color:var(--text);position:relative}
.abs{position:absolute}
.hero{left:0;top:0;width:983px;height:365px;background:linear-gradient(180deg,var(--hero-top) 0%,var(--hero-bottom) 70%,#8fb9df 100%)}
.brand{left:39px;top:138px;display:flex;align-items:center;gap:10px;font-weight:700;font-size:25px;letter-spacing:3px;text-transform:uppercase;color:#fff}
.brand-mark{width:14px;height:14px;background:var(--lime)}
.search{left:53px;top:259px;width:889px;height:98px;background:#fff;border:4px solid #2d8fd6;border-radius:6px}
.search label{position:absolute;top:22px;font-size:14px;font-weight:600;color:#222}
.search .field{position:absolute;top:40px;height:30px;border:1px solid #b9b9b9;background:#fff}
.search .btn{position:absolute;left:738px;top:38px;width:117px;height:33px;background:var(--lime);color:#fff;font-size:17px;font-weight:600;text-align:center;line-height:33px;letter-spacing:1px}
.card{left:39px;top:378px;width:541px;height:568px;background:var(--card-bg)}
.card::after{content:"";position:absolute;right:-14px;top:8px;width:14px;height:552px;background:#d4d5d7}
.person-name{left:30px;top:12px;font-size:28px;font-weight:700;color:var(--brand-blue)}
.age{left:340px;top:22px;font-size:15px;font-weight:600;color:#555}
.name-rule{left:30px;top:52px;width:340px;height:3px;background:var(--brand-blue)}
.row{left:30px;display:flex;align-items:center;gap:22px;font-size:16px;color:#444}
.row svg{width:24px;height:24px;flex:none}
.row a{color:var(--teal-dark);text-decoration:none}
.more-btn{left:391px;top:62px;width:102px;height:27px;background:var(--teal);color:#fff;font-size:14px;font-weight:600;text-align:center;line-height:27px;border-radius:2px}
.section-rule{left:30px;top:285px;width:475px;height:1px;background:var(--rule)}
.col-head{top:298px;font-size:14px;line-height:16px;color:var(--teal-dark)}
.col-list{top:350px;list-style:none;font-size:12px;line-height:15.5px;color:#444}
.col-divider{top:295px;width:1px;height:250px;background:var(--rule)}
.addr-list{list-style:none;counter-reset:a}
.addr-list li{counter-increment:a;padding-left:14px;position:relative;margin-bottom:6px}
.addr-list li::before{content:counter(a) ".";position:absolute;left:0}
.map{border:5px solid #d3d4d6;background:var(--map-street)}
.map-street{left:644px;top:380px;width:267px;height:267px;background:linear-gradient(160deg,#ece7da,#d8d1c1)}
.map-aerial{left:667px;top:667px;width:265px;height:265px;background:linear-gradient(150deg,#7c8763,#5d6a4c 60%,#8a8b7c)}
.green-line{left:0;top:948px;width:983px;height:8px;background:var(--green-line)}
.promo-left{left:39px;top:975px;width:533px;height:152px;background:var(--teal);color:#fff;overflow:hidden}
.promo-left h2{position:absolute;left:18px;top:10px;font-size:19px;font-weight:600;color:#e7f36a}
.promo-left h2 span{color:#fff;font-weight:700}
.ticks{position:absolute;top:44px;list-style:none;font-size:14px;line-height:20px}
.ticks li{display:flex;align-items:center;gap:10px}
.ticks svg{width:14px;height:12px}
.promo-btn{position:absolute;background:var(--lime);color:#fff;text-align:center;font-size:17px;font-weight:600;border-radius:3px}
.promo-left .promo-btn{left:101px;top:110px;width:326px;height:32px;line-height:32px}
.deco-lens{position:absolute;left:318px;top:-20px;width:170px;height:170px;opacity:.18}
.promo-right{left:591px;top:975px;width:351px;height:152px;background:var(--promo-blue);color:#fff}
.promo-right h2{position:absolute;left:18px;top:10px;font-size:19px;font-weight:600}
.promo-right p{position:absolute;left:18px;top:42px;width:320px;font-size:13px;line-height:18px}
.promo-right .promo-btn{left:43px;top:110px;width:263px;height:32px;line-height:32px;background:var(--teal)}
.footer-nav{left:0;top:1148px;width:983px;text-align:center;font-size:13px;color:var(--brand-blue)}
.footer-nav span{color:#888;margin:0 8px}
.copyright{left:0;top:1168px;width:983px;text-align:center;font-size:11px;color:#777}
</style>
</head>
<body>
<div class="abs hero" role="img" aria-label="Banner photo of smiling people in blue tones"></div>
<div class="abs brand"><span>Kestrel Lineage Lookups</span><span class="brand-mark"></span></div>

<form class="abs search">
  <label style="left:14px">First Name</label><span class="field" style="left:14px;width:163px"></span>
  <label style="left:193px">M.I.</label><span class="field" style="left:193px;width:34px"></span>
  <label style="left:242px">Last Name</label><span class="field" style="left:242px;width:200px"></span>
  <label style="left:454px">City</label><span class="field" style="left:454px;width:143px"></span>
  <label style="left:606px">State</label><span class="field" style="left:606px;width:117px"></span>
  <span class="btn">SEARCH</span>
</form>

<section class="abs card">
  <h1 class="abs person-name">Marisol K Whitaker</h1>
  <div class="abs age">Age: 45</div>
  <div class="abs name-rule"></div>

  <div class="abs row" style="top:66px">
    <svg viewBox="0 0 24 24"><path d="M6 2l4 4-2 3c1 3 4 6 7 7l3-2 4 4-3 3C10 21 3 14 3 5z" fill="#333"/></svg>
    <span>(555) 214-0387</span>
  </div>
  <div class="abs more-btn">More Info...</div>

  <div class="abs row" style="top:105px">
    <svg viewBox="0 0 24 24"><path d="M12 2L1 12h3v10h6v-6h4v6h6V12h3z" fill="#333"/></svg>
    <span>42 Larkin Ave Brookfield, NY 10219</span>
  </div>

  <div class="abs row" style="top:145px;align-items:flex-start">
    <svg viewBox="0 0 24 24"><rect x="1" y="5" width="22" height="15" fill="#333"/><path d="M1 5l11 9 11-9" fill="none" stroke="#fff" stroke-width="1.5"/></svg>
    <span style="line-height:20px;font-size:15px">mkw77sky@northlinkmail.net<br>whitakerm@northlinkmail.net</span>
  </div>

  <div class="abs row" style="top:205px">
    <svg viewBox="0 0 24 24"><circle cx="8" cy="7" r="4" fill="#333"/><path d="M0 21c0-6 4-9 8-9s8 3 8 9z" fill="#333"/><circle cx="17" cy="9" r="3.5" fill="#333"/><path d="M12 21c1-5 3-8 5-8s7 2 7 8z" fill="#333"/></svg>
    <a>Check Nationwide Criminal Records for Marisol K Whitaker &gt;&gt;</a>
  </div>
  <div class="abs row" style="top:246px">
    <svg viewBox="0 0 24 24"><circle cx="14" cy="9" r="7" fill="none" stroke="#333" stroke-width="3"/><path d="M9 14l-7 7" stroke="#333" stroke-width="4"/></svg>
    <a>Advanced Background Report on Marisol K Whitaker &gt;&gt;</a>
  </div>

  <div class="abs section-rule"></div>

  <div class="abs col-head" style="left:47px">Possible<br>Relatives:</div>
  <ul class="abs col-list" style="left:47px">
    <li>Oliver Grant Whitaker</li><li>Harlan P Whitaker</li><li>Tessa R Whitaker</li>
    <li>Nora L Whitaker</li><li>Celia M Whitaker</li><li>Wade D Whitaker</li>
    <li>Rory J Whitaker</li><li>Elliot Dean Whitaker</li><li>Ivy K Whitaker</li>
  </ul>
  <div class="abs col-divider" style="left:176px"></div>

  <div class="abs col-head" style="left:197px">Previous Phone<br>Numbers:</div>
  <ol class="abs col-list addr-list" style="left:197px">
    <li style="margin:0">(555) 214-0387</li><li style="margin:0">(555) 314-2270</li>
    <li style="margin:0">(555) 407-6612</li><li style="margin:0">(555) 981-5530</li>
  </ol>
  <div class="abs col-divider" style="left:318px"></div>

  <div class="abs col-head" style="left:334px">Previous<br>Addresses:</div>
  <ol class="abs col-list addr-list" style="left:334px;width:170px">
    <li>18 Mercer St.,<br>Brookfield, NY 10213</li>
    <li>311 Ashby Rd #4,<br>Brookfield, NY 10207</li>
    <li>64 Fenwick Pl,<br>Brookfield, NY 10208</li>
    <li>205 Orchard Ave,<br>Brookfield, NY 10219</li>
    <li>77 Delmont St.,<br>Brookfield, NY 10211</li>
    <li>None, Brookfield, NY 10208</li>
  </ol>
</section>

<div class="abs map map-street" role="img" aria-label="Street map centred on the current address"></div>
<div class="abs map map-aerial" role="img" aria-label="Aerial view of the current address"></div>

<div class="abs green-line"></div>

<section class="abs promo-left">
  <svg class="deco-lens" viewBox="0 0 100 100"><circle cx="45" cy="40" r="30" fill="none" stroke="#fff" stroke-width="12"/><path d="M66 62l28 30" stroke="#fff" stroke-width="14"/></svg>
  <h2>Want more in-depth information on <span>Marisol K Whitaker</span> ?</h2>
  <ul class="ticks" style="left:18px">
    <li><svg viewBox="0 0 14 12"><path d="M1 6l4 4 8-9" fill="none" stroke="#fff" stroke-width="2.5"/></svg>Name and AKAs</li>
    <li><svg viewBox="0 0 14 12"><path d="M1 6l4 4 8-9" fill="none" stroke="#fff" stroke-width="2.5"/></svg>Up to 40-year address history</li>
    <li><svg viewBox="0 0 14 12"><path d="M1 6l4 4 8-9" fill="none" stroke="#fff" stroke-width="2.5"/></svg>Date of birth</li>
  </ul>
  <ul class="ticks" style="left:250px">
    <li><svg viewBox="0 0 14 12"><path d="M1 6l4 4 8-9" fill="none" stroke="#fff" stroke-width="2.5"/></svg>Evictions &amp; bankrupcy</li>
    <li><svg viewBox="0 0 14 12"><path d="M1 6l4 4 8-9" fill="none" stroke="#fff" stroke-width="2.5"/></svg>Property records</li>
    <li><svg viewBox="0 0 14 12"><path d="M1 6l4 4 8-9" fill="none" stroke="#fff" stroke-width="2.5"/></svg>Criminal records check</li>
  </ul>
  <div class="promo-btn">Get advanced background report...</div>
</section>

<section class="abs promo-right">
  <h2>What's in your background report?</h2>
  <p>See what records are publicly available in your background report. Also, check out the public records in reports for your friends and family.</p>
  <div class="promo-btn">Check my background report...</div>
</section>

<nav class="abs footer-nav">Home<span>|</span>People<span>|</span>Directory<span>|</span>Privacy<span>|</span>Terms<span>|</span>Contact Us</nav>
<div class="abs copyright">Copyright © 2012 KestrelLineageLookups.com</div>
</body>
</html>
```